Delmer's Pressure Washing Services

Starting a pressure washing business on my own in Central Valley California, not too much experience so affordable, I do houses, fences, driveways, cars, trailers, RVs. Planning to make this full-time hoping clientele picks up after having a nice business card. Design doesn't have to be flashy, more to the point, I like simplistic/personable. I do not want something exhausting to look at or with too much going on.

Target Market(s)

Residential, Commercial

Industry/Entity Type

Pressure Washing

Contact Information for Business Card

avalible Services

Font styles to use
Sans Serif

Colors
0054AA
0677BA
7BADD7
CADEEF
E8F1F8
0094D4
00A9DD
6FCCEA
C7EBF8
E9F6FB
00AB8E
00BBA5
67D7C9
C6EFE9
E9F9F6

```html
<!DOCTYPE html>
<html lang="en">
<head>
<meta charset="UTF-8">
<title>Delmer's Pressure Washing Services – Business Card</title>
<link rel="stylesheet" href="https://fonts.googleapis.com/css2?family=Montserrat:wght@500;600;700&family=Open+Sans:wght@400;600&display=swap">
<style>
  :root {
    --navy: #1e4f8f;
    --teal: #36ab98;
    --stripe: #4d82c8;
    --ink: #3a3a3a;
    --paper: #ffffff;
    --tint: #f6f8fa;
    --backdrop: #ededed;
  }
  * { margin: 0; padding: 0; box-sizing: border-box; }
  html, body { width: 848px; height: 1200px; overflow: hidden; }
  body {
    background: var(--backdrop);
    position: relative;
    font-family: "Open Sans", Arial, sans-serif;
  }
  .card {
    position: absolute;
    left: 151px;
    width: 547px;
    height: 321px;
    background: var(--paper);
    overflow: hidden;
  }
  .card--front { top: 245px; }
  .card--back { top: 633px; }
  .card__pattern {
    position: absolute;
    inset: 20px 0;
    background: var(--tint);
  }
  .card--back .card__pattern { left: 270px; }
  .card__bands {
    position: absolute;
    inset: 0;
    width: 547px;
    height: 321px;
  }
  .wordmark {
    position: absolute;
    font-family: "Montserrat", Arial, sans-serif;
    font-weight: 600;
    color: var(--navy);
    font-size: 19px;
    line-height: 1.25;
    text-align: center;
    letter-spacing: 0.2px;
  }
  .card--front .wordmark { left: 0; right: 0; top: 132px; }
  .card--back .wordmark { left: 300px; width: 240px; top: 148px; font-size: 17px; }
  .holder {
    position: absolute;
    left: 65px;
    top: 70px;
  }
  .holder__name {
    font-family: "Montserrat", Arial, sans-serif;
    font-weight: 700;
    font-size: 26px;
    letter-spacing: 0.5px;
    color: var(--navy);
    line-height: 1;
  }
  .holder__name .surname { color: var(--teal); }
  .holder__role {
    margin-top: 12px;
    font-family: "Montserrat", Arial, sans-serif;
    font-weight: 600;
    font-size: 11px;
    color: var(--ink);
    letter-spacing: 0.3px;
  }
  .contacts {
    position: absolute;
    left: 68px;
    top: 151px;
    list-style: none;
  }
  .contacts__item {
    display: flex;
    align-items: flex-start;
    gap: 8px;
    font-size: 11.5px;
    color: var(--ink);
    line-height: 1.45;
    margin-bottom: 8px;
  }
  .contacts__icon { width: 11px; height: 11px; margin-top: 3px; flex: none; fill: var(--teal); }
</style>
</head>
<body>

<section class="card card--front">
  <div class="card__pattern" role="img" aria-label="Faint background pattern of cleaning icons"></div>
  <svg class="card__bands" viewBox="0 0 547 321" aria-hidden="true">
    <polygon points="0,0 326,0 340,20 0,20" fill="var(--navy)"/>
    <polygon points="332,0 342,0 356,20 346,20" fill="var(--stripe)"/>
    <polygon points="348,0 358,0 372,20 362,20" fill="var(--stripe)"/>
    <polygon points="364,0 547,0 547,20 378,20" fill="var(--teal)"/>
    <polygon points="0,301 168,301 182,321 0,321" fill="var(--teal)"/>
    <polygon points="172,301 182,301 196,321 186,321" fill="var(--stripe)"/>
    <polygon points="188,301 198,301 212,321 202,321" fill="var(--stripe)"/>
    <polygon points="204,301 547,301 547,321 218,321" fill="var(--navy)"/>
  </svg>
  <p class="wordmark">Delmer's<br>Pressure Washing Services</p>
</section>

<section class="card card--back">
  <div class="card__pattern" role="img" aria-label="Faint background pattern of cleaning icons"></div>
  <svg class="card__bands" viewBox="0 0 547 321" aria-hidden="true">
    <polygon points="0,0 210,0 196,20 0,20" fill="var(--teal)"/>
    <polygon points="214,0 224,0 210,20 200,20" fill="var(--stripe)"/>
    <polygon points="228,0 238,0 224,20 214,20" fill="var(--stripe)"/>
    <polygon points="242,0 547,0 547,20 228,20" fill="var(--navy)"/>
    <polygon points="0,301 292,301 278,321 0,321" fill="var(--navy)"/>
    <polygon points="296,301 306,301 292,321 282,321" fill="var(--stripe)"/>
    <polygon points="310,301 320,301 306,321 296,321" fill="var(--stripe)"/>
    <polygon points="324,301 547,301 547,321 310,321" fill="var(--teal)"/>
  </svg>

  <div class="holder">
    <h1 class="holder__name">DELMER <span class="surname">ORTEGA</span></h1>
    <p class="holder__role">CEO &amp;OWNER</p>
  </div>

  <ul class="contacts">
    <li class="contacts__item">
      <svg class="contacts__icon" viewBox="0 0 24 24"><path d="M6.6 10.8a15.1 15.1 0 0 0 6.6 6.6l2.2-2.2a1 1 0 0 1 1-.25 11.4 11.4 0 0 0 3.6.57 1 1 0 0 1 1 1V20a1 1 0 0 1-1 1A17 17 0 0 1 3 4a1 1 0 0 1 1-1h3.5a1 1 0 0 1 1 1c0 1.25.2 2.45.57 3.57a1 1 0 0 1-.25 1z"/></svg>
      <span>2095550142</span>
    </li>
    <li class="contacts__item">
      <svg class="contacts__icon" viewBox="0 0 24 24"><path d="M12 2a10 10 0 1 0 0 20 10 10 0 0 0 0-20zm6.9 6h-2.9a15.7 15.7 0 0 0-1.4-3.6A8 8 0 0 1 18.9 8zM12 4a14 14 0 0 1 1.9 4h-3.8A14 14 0 0 1 12 4zM4.3 14a8.2 8.2 0 0 1 0-4h3.4a16.5 16.5 0 0 0 0 4zm.8 2h2.9a15.7 15.7 0 0 0 1.4 3.6A8 8 0 0 1 5.1 16zM8 8H5.1a8 8 0 0 1 4.3-3.6A15.7 15.7 0 0 0 8 8zm4 12a14 14 0 0 1-1.9-4h3.8A14 14 0 0 1 12 20zm2.3-6H9.7a14.7 14.7 0 0 1 0-4h4.6a14.7 14.7 0 0 1 0 4zm.3 5.6A15.7 15.7 0 0 0 16 16h2.9a8 8 0 0 1-4.3 3.6zm1.7-5.6a16.5 16.5 0 0 0 0-4h3.4a8.2 8.2 0 0 1 0 4z"/></svg>
      <span>www.delmerwash.com</span>
    </li>
    <li class="contacts__item">
      <svg class="contacts__icon" viewBox="0 0 24 24"><path d="M2 5h20v14H2zm10 7.5L20 7H4z"/></svg>
      <span>hello@delmerwash.com</span>
    </li>
    <li class="contacts__item">
      <svg class="contacts__icon" viewBox="0 0 24 24"><path d="M12 2a7 7 0 0 0-7 7c0 5.2 7 13 7 13s7-7.8 7-13a7 7 0 0 0-7-7zm0 9.5A2.5 2.5 0 1 1 12 6.5a2.5 2.5 0 0 1 0 5z"/></svg>
      <span>48 Orchard Lane, Modesto,<br>CA 95350</span>
    </li>
  </ul>

  <p class="wordmark">Delmer's<br>Pressure Washing Services</p>
</section>

</body>
</html>
```